Brightvale Crew Word Press Website

We need a graphical, fun website that conveys our messaging of providing the Best-In-Class Signature Marketing System for Mortgage Loan Officers and Realtors. Our system uses AI and Predictive Analysis to uncover the 'Gold' hidden in contact databases. The 'Gold' is defined as people who are in the market or likely to be in the market soon. We place that 'Gold' in the form of Contact Name, Address, Phone and Email on a Daily To Do List detailing what type of contact should be made.

Target Market(s)

Mortgage Loan Officers and Realtors

Industry/Entity Type

Mortgage & Real Estate

Coding

Coded - Design and coding required

Number of Pages Required

5+ page

Requirements
Must have
• I like the look of this site- https://www.homeloanpromostudio.example/
Nice to have
• Please create a flow that is similar to https://www.homeloanpromostudio.example/, but better, more dynamic. Site must be responsive and mobile friendly. Site will have embedded videos. Site need to convey a message of hope, imagination, innovation, results oriented, better than the rest, victory!
Should not have
• Nothing cheesy or low class.

```html
<!DOCTYPE html>
<html lang="en">
<head>
<meta charset="utf-8">
<title>Brightvale Crew – Website Pages</title>
<link href="https://fonts.googleapis.com/css2?family=Montserrat:wght@300;400;500;600;700;800&display=swap" rel="stylesheet">
<style>
:root{
  --blue:#12329e;
  --blue-deep:#0a2584;
  --blue-light:#1e4bc6;
  --yellow:#f4d03c;
  --yellow-soft:#f6e69a;
  --navy:#1f2135;
  --ink:#1d2140;
  --grey:#8d92a5;
  --line:#d9dee8;
  --mist:#f3f5f9;
  --title:#c5ccd9;
  --white:#ffffff;
}
*{box-sizing:border-box;margin:0;padding:0}
html,body{width:1200px;height:3750px;overflow:hidden}
body{position:relative;background:var(--white);font-family:'Montserrat',sans-serif;color:var(--ink)}
.abs{position:absolute}
.backdrop{position:absolute;left:0;top:0;width:1200px;height:480px}
.page-title{position:absolute;font-weight:600;font-size:52px;color:var(--title);letter-spacing:1px;transform:translateX(-50%);white-space:nowrap}

.mock{position:absolute;background:var(--white);overflow:hidden;box-shadow:0 6px 24px rgba(20,30,70,.12)}
.mock--home{left:315px;top:112px;width:573px;height:1540px;font-size:8px}
.mock--about{left:66px;top:2101px;width:451px;height:1219px;font-size:6.4px}
.mock--contact{left:630px;top:1900px;width:454px;height:383px;font-size:6.4px}
.mock--services{left:684px;top:2472px;width:453px;height:1251px;font-size:6.4px}

/* navigation */
.site-nav{position:absolute;left:0;top:0;width:100%;height:4.6em;z-index:3}
.brand{position:absolute;display:flex;align-items:center;gap:.5em;font-weight:700;letter-spacing:.06em;white-space:nowrap}
.brand-dot{width:1.5em;height:1.5em;border-radius:50%;background:var(--yellow);display:block}
.site-nav .brand{left:13.5%;top:1.7em;font-size:1em;color:var(--white)}
.nav-links{position:absolute;left:44%;top:2.15em;display:flex;gap:1.6em;list-style:none;font-size:.6em;font-weight:600;color:var(--white);align-items:center}
.nav-links .is-cta{border:1px solid rgba(255,255,255,.5);padding:.4em 1em;background:rgba(255,255,255,.12)}
.nav-phone{position:absolute;left:77%;top:2.1em;font-size:.62em;font-weight:600;color:var(--white);display:flex;gap:.4em;align-items:center}
.nav-phone svg{width:1.1em;height:1.1em}
.site-nav--light .brand,.site-nav--light .nav-links,.site-nav--light .nav-phone{color:var(--ink)}
.site-nav--light .nav-links .is-cta{border-color:var(--line);background:var(--mist)}

/* footer */
.site-footer{position:absolute;left:0;bottom:0;width:100%;background:var(--navy);color:#b7bbcb}
.foot-brand{position:absolute;left:9%;top:34%;display:flex;flex-direction:column;align-items:center;gap:.6em;color:var(--white);font-weight:700;font-size:1em;letter-spacing:.06em}
.foot-brand .brand-dot{width:2.2em;height:2.2em}
.foot-contact{position:absolute;left:36.5%;top:16%;font-size:.55em;line-height:1.6}
.foot-contact b{color:var(--white);font-weight:600;display:block}
.foot-row{display:flex;gap:.6em;align-items:flex-start;margin-bottom:.7em}
.foot-row svg{width:1.1em;height:1.1em;flex:none;margin-top:.2em}
.foot-row .big{color:var(--white);font-size:1.25em;font-weight:600}
.foot-links{position:absolute;left:62%;top:16%;list-style:none;font-size:.55em;line-height:2}
.foot-social{position:absolute;left:77%;top:38%;display:flex;gap:.9em}
.foot-social i{width:.8em;height:.8em;border-radius:50%;background:#cfd3e0;display:block}
.foot-copy{position:absolute;left:77%;top:56%;font-size:.45em}

/* shared */
.hero-svg{position:absolute;left:0;top:0}
.img-block{position:absolute;border-radius:3px}
.img-photo{background:linear-gradient(135deg,#c9ccd2 0%,#8a8f99 45%,#3c4150 100%)}
.img-device{background:linear-gradient(160deg,#ffffff 0%,#e6ebf4 60%,#c7cfdd 100%);border-radius:6px;box-shadow:0 8px 20px rgba(0,0,0,.18)}
.section-title{position:absolute;transform:translateX(-50%);font-weight:600;white-space:nowrap;letter-spacing:.03em;color:var(--ink)}
.tiny{font-size:.55em;line-height:1.65;color:var(--grey)}
.btn{position:absolute;background:var(--yellow);color:var(--ink);font-weight:700;font-size:.55em;display:flex;align-items:center;justify-content:center;letter-spacing:.05em}
.btn--blue{background:#1a8be0;color:var(--white)}

/* home */
.hero-copy{position:absolute;left:79px;top:80px;color:var(--white)}
.hero-copy h1{font-size:19px;line-height:22px;font-weight:400;letter-spacing:.02em}
.hero-copy h1 strong{font-weight:700;display:block}
.hero-copy p{font-size:8px;line-height:12px;margin-top:12px;letter-spacing:.03em}
.badges{position:absolute;top:297px;left:0;width:100%;display:flex;justify-content:center;gap:44px;color:var(--white)}
.badge{display:flex;gap:5px;align-items:center;font-size:5.4px;font-weight:700;line-height:1.3}
.badge svg{width:10px;height:10px}
.badge small{display:block;color:var(--yellow);font-size:5px;font-weight:600}
.stat{position:absolute;transform:translateX(-50%);text-align:center;top:406px;white-space:nowrap}
.stat strong{display:block;color:#2a6fe0;font-size:19px;line-height:22px;font-weight:700}
.stat strong.stars{color:var(--yellow);font-size:10px;line-height:22px;letter-spacing:1px}
.stat span{display:block;margin-top:3px;font-size:4.6px;color:var(--grey);letter-spacing:.05em}
.stat-sep{position:absolute;top:408px;width:1px;height:30px;background:var(--line)}
.service-label{position:absolute;width:120px}
.service-label h4{font-size:6px;font-weight:700;color:var(--ink);margin-bottom:3px;letter-spacing:.02em}
.service-label p{font-size:5.2px;line-height:1.6;color:var(--grey)}
.service-label.right{text-align:right}
.service-label.center{text-align:center;transform:translateX(-50%)}
.orbit-icon{position:absolute;width:22px;height:22px;margin:-11px 0 0 -11px;border-radius:50%;background:var(--white);border:1.5px solid #c7d3ef;display:flex;align-items:center;justify-content:center}
.orbit-icon i{width:9px;height:9px;border:1.4px solid var(--blue);border-radius:2px;display:block}
.form-field{position:absolute;left:312px;width:151px;height:18px;border:1px solid rgba(255,255,255,.55);color:var(--white);font-size:4.6px;padding:6px 5px;letter-spacing:.05em}

/* about */
.team-name{position:absolute;font-size:6.5px;font-weight:700}
.value-item{position:absolute;left:243px;width:133px;height:22px;background:var(--white);box-shadow:0 2px 6px rgba(20,30,70,.08);border-left:2px solid var(--blue);font-size:4.8px;font-weight:700;padding:8px 9px;color:var(--ink)}
.value-item::after{content:"";position:absolute;right:7px;top:7px;width:7px;height:7px;border-radius:50%;background:var(--line)}
.social-dots{position:absolute;display:flex;gap:4px}
.social-dots i{width:8px;height:8px;border-radius:50%;background:var(--blue);display:block}
.cta-card{position:absolute;background:var(--white);box-shadow:0 6px 18px rgba(20,30,70,.12);text-align:center;z-index:2;border-radius:2px}
.cta-card h3{font-size:11px;font-weight:500;margin-top:26px}
.cta-card p{font-size:4.6px;color:var(--grey);line-height:1.6;margin:6px auto 0;width:60%}
.cta-card .btn{left:50%;transform:translateX(-50%);width:44px;height:11px;font-size:3.6px;bottom:16px}

/* services */
.svc-card{position:absolute;width:168px;height:175px;background:var(--white);box-shadow:0 4px 14px rgba(20,30,70,.09);padding:32px 14px 0}
.svc-card svg{width:26px;height:24px;display:block;margin-bottom:8px}
.svc-card h4{font-size:4.8px;font-weight:700;letter-spacing:.03em;margin-bottom:5px}
.svc-card .lead{font-size:4.8px;line-height:1.6;color:var(--ink);margin-bottom:6px}
.svc-card p{font-size:4.2px;line-height:1.7;color:var(--grey)}

/* contact */
.contact-card{position:absolute;left:52px;top:102px;width:351px;height:165px;background:var(--white);box-shadow:0 6px 18px rgba(20,30,70,.12)}
.contact-panel{position:absolute;left:0;top:0;width:118px;height:165px;background:linear-gradient(180deg,var(--blue-light),var(--blue-deep));color:var(--white);padding:22px 14px}
.contact-panel h4{font-size:7.5px;font-weight:600;line-height:1.35;margin-bottom:6px}
.contact-panel p{font-size:4.3px;line-height:1.7;color:#c8d2f2}
.contact-input{position:absolute;border:1px solid var(--line);font-size:4px;color:var(--grey);padding:4px 5px}
</style>
</head>
<body>

<svg class="backdrop" width="1200" height="480" viewBox="0 0 1200 480" aria-hidden="true">
  <defs>
    <linearGradient id="sun" x1="0" y1="0" x2="1" y2="1">
      <stop offset="0" stop-color="#f1e36f"/>
      <stop offset="1" stop-color="#f6eca8"/>
    </linearGradient>
  </defs>
  <path d="M0 0H1200V465Q700 300 0 420Z" fill="url(#sun)"/>
</svg>

<div class="page-title" style="left:611px;top:28px">Home</div>
<div class="page-title" style="left:292px;top:1900px">About us</div>
<div class="page-title" style="left:857px;top:1782px">Contact us</div>
<div class="page-title" style="left:910px;top:2384px">Services</div>

<!-- HOME -->
<section class="mock mock--home" aria-label="Home page">
  <svg class="hero-svg" width="573" height="360" viewBox="0 0 573 360" aria-hidden="true">
    <defs>
      <linearGradient id="heroBlue" x1="0" y1="0" x2="1" y2="1">
        <stop offset="0" stop-color="#0f2d95"/>
        <stop offset="1" stop-color="#1b45bd"/>
      </linearGradient>
    </defs>
    <path d="M0 0H573V318Q286 360 0 318Z" fill="url(#heroBlue)"/>
  </svg>

  <nav class="site-nav">
    <div class="brand"><span class="brand-dot"></span>BRIGHTVALE CREW</div>
    <ul class="nav-links"><li>HOME</li><li>ABOUT</li><li>SERVICES</li><li>BLOG</li><li class="is-cta">CONTACT</li></ul>
    <div class="nav-phone"><svg viewBox="0 0 12 12"><path d="M3 1l2 2.5-1.2 1.3a7 7 0 003.4 3.4L8.5 7 11 9l-1.4 1.8C5 10.5 1.5 7 1.2 2.4z" fill="currentColor"/></svg>123-456-7890</div>
  </nav>

  <div class="hero-copy">
    <h1>FIND THE RIGHT<strong>MORTGAGE</strong><strong>OPTION FOR YOU!</strong></h1>
    <p>Big Dreams Even Bigger And<br>Better Loans.</p>
  </div>
  <div class="btn" style="left:79px;top:188px;width:79px;height:20px">GET STARTED</div>
  <div class="img-block img-device" role="img" aria-label="Desktop monitor showing a mortgage analytics dashboard" style="left:341px;top:72px;width:160px;height:178px"></div>

  <div class="badges">
    <div class="badge"><svg viewBox="0 0 10 10"><circle cx="5" cy="4" r="3" fill="none" stroke="#f4d03c"/><path d="M3.5 6.5L3 9.5 5 8.5 7 9.5 6.5 6.5" fill="none" stroke="#f4d03c"/></svg><div><small>AWARDED</small>TOP RATED</div></div>
    <div class="badge"><svg viewBox="0 0 10 10"><rect x="1" y="3" width="8" height="6" fill="none" stroke="#f4d03c"/><path d="M3.5 3V1.5h3V3" fill="none" stroke="#f4d03c"/></svg><div><small>100%</small>JOB SUCCESS</div></div>
    <div class="badge"><svg viewBox="0 0 10 10"><path d="M5 .8l1.3 2.7 3 .4-2.2 2.1.5 3L5 7.6 2.4 9l.5-3L.7 3.9l3-.4z" fill="none" stroke="#f4d03c"/></svg><div><small>CUSTOMER</small>RATING</div></div>
  </div>

  <div class="section-title" style="left:286px;top:372px;font-size:12px">OUR SUCCESS STORIES</div>
  <div class="stat" style="left:150px"><strong>23</strong><span>PROJECTS</span></div>
  <div class="stat-sep" style="left:196px"></div>
  <div class="stat" style="left:242px"><strong>7,006</strong><span>DEVELOPMENT HOURS</span></div>
  <div class="stat-sep" style="left:287px"></div>
  <div class="stat" style="left:332px"><strong>100%</strong><span>JOB COMPLETION</span></div>
  <div class="stat-sep" style="left:378px"></div>
  <div class="stat" style="left:425px"><strong class="stars">★★★★★</strong><span>CUSTOMER RATING</span></div>

  <div class="section-title" style="left:286px;top:470px;font-size:12px">OUR SERVICES</div>
  <div class="service-label center" style="left:285px;top:498px"><h4>EMAIL MARKETING</h4><p>Lorem ipsum dolor sit amet,<br>consectetuer adipiscing elit.</p></div>
  <div class="service-label right" style="left:86px;top:547px"><h4>BRAND DESIGN &amp; STRATEGY</h4><p>Lorem ipsum dolor sit amet,<br>consectetuer adipiscing elit.</p></div>
  <div class="service-label" style="left:362px;top:550px"><h4>WEBSITE DEVELOPMENT</h4><p>Lorem ipsum dolor sit amet,<br>consectetuer adipiscing elit.</p></div>
  <div class="service-label right" style="left:72px;top:604px"><h4>SOCIAL MEDIA MANAGEMENT</h4><p>Lorem ipsum dolor sit amet,<br>consectetuer adipiscing elit.</p></div>
  <div class="service-label" style="left:376px;top:606px"><h4>REPUTATION MANAGEMENT</h4><p>Lorem ipsum dolor sit amet,<br>consectetuer adipiscing elit.</p></div>
  <div class="service-label right" style="left:86px;top:662px"><h4>MORTGAGE CHATBOT</h4><p>Lorem ipsum dolor sit amet,<br>consectetuer adipiscing elit.</p></div>
  <div class="service-label" style="left:358px;top:662px"><h4>CONTENT MARKETING</h4><p>Lorem ipsum dolor sit amet,<br>consectetuer adipiscing elit.</p></div>
  <div class="service-label center" style="left:285px;top:709px"><h4>SEO</h4><p>Lorem ipsum dolor sit amet,<br>consectetuer adipiscing elit.</p></div>

  <svg class="abs" style="left:205px;top:536px" width="160" height="160" viewBox="0 0 160 160" aria-hidden="true">
    <defs>
      <radialGradient id="hub" cx=".4" cy=".35" r=".7">
        <stop offset="0" stop-color="#2454d0"/>
        <stop offset="1" stop-color="#0c2a8c"/>
      </radialGradient>
    </defs>
    <circle cx="80" cy="80" r="73" fill="url(#hub)"/>
    <circle cx="80" cy="80" r="11" fill="#f4d03c"/>
  </svg>
  <div class="orbit-icon" style="left:285px;top:551px"><i></i></div>
  <div class="orbit-icon" style="left:339px;top:570px"><i></i></div>
  <div class="orbit-icon" style="left:357px;top:616px"><i></i></div>
  <div class="orbit-icon" style="left:335px;top:669px"><i></i></div>
  <div class="orbit-icon" style="left:285px;top:686px"><i></i></div>
  <div class="orbit-icon" style="left:239px;top:669px"><i></i></div>
  <div class="orbit-icon" style="left:220px;top:616px"><i></i></div>
  <div class="orbit-icon" style="left:233px;top:570px"><i></i></div>

  <div class="abs" style="left:0;top:759px;width:573px;height:378px;background:var(--mist)"></div>
  <div class="img-block img-photo" role="img" aria-label="Video still of a man working at a desktop computer in an office, with a yellow play button" style="left:127px;top:795px;width:320px;height:185px;border-radius:0"></div>
  <div class="section-title" style="left:286px;top:1020px;font-size:12px">ABOUT US</div>
  <p class="abs" style="left:160px;top:1046px;width:253px;text-align:center;font-size:5.4px;line-height:1.7;color:var(--grey)">Lorem ipsum dolor sit amet, consectetuer adipiscing elit, sed diam nonummy nibh euismod tincidunt ut laoreet dolore magna aliquam erat volutpat. Ut wisi enim ad minim veniam, quis nostrud exerci tation ullamcorper suscipit lobortis nisl ut aliquip ex ea commodo consequat.</p>
  <div class="abs" style="left:254px;top:1100px;font-size:5.4px;font-weight:700;color:#2a6fe0;display:flex;gap:5px;align-items:center">READ MORE <svg width="20" height="5" viewBox="0 0 20 5"><path d="M0 2.5H18M16 .5l2 2-2 2" stroke="#2a6fe0" fill="none" stroke-width=".8"/></svg></div>

  <svg class="abs" style="left:0;top:1137px" width="573" height="214" viewBox="0 0 573 214" aria-hidden="true">
    <defs>
      <linearGradient id="touchBlue" x1="0" y1="0" x2="1" y2="1">
        <stop offset="0" stop-color="#0c2a8c"/>
        <stop offset="1" stop-color="#1a44bb"/>
      </linearGradient>
    </defs>
    <path d="M573 0H200Q78 8 78 128Q78 214 200 214H573Z" fill="url(#touchBlue)"/>
  </svg>
  <div class="img-block img-device" role="img" aria-label="White desktop monitor with keyboard showing a reporting dashboard" style="left:72px;top:1170px;width:240px;height:220px"></div>
  <div class="section-title" style="left:387px;top:1170px;font-size:11px;color:var(--white);font-weight:500">GET IN TOUCH</div>
  <div class="form-field" style="top:1198px">NAME</div>
  <div class="form-field" style="top:1226px">PHONE</div>
  <div class="form-field" style="top:1254px">EMAIL</div>
  <div class="btn" style="left:347px;top:1291px;width:80px;height:19px;font-size:4.6px">GET STARTED</div>

  <footer class="site-footer" style="height:116px">
    <div class="foot-brand"><span class="brand-dot"></span>BRIGHTVALE CREW</div>
    <div class="foot-contact">
      <div class="foot-row"><svg viewBox="0 0 10 10"><path d="M5 9.5S1.5 5.8 1.5 3.8a3.5 3.5 0 017 0C8.5 5.8 5 9.5 5 9.5z" fill="#fff"/></svg><div><b>BRIGHTVALE CREW</b>Lorem ipsum sit dolor sit<br>amet adipiscing, 1200</div></div>
      <div class="foot-row"><svg viewBox="0 0 12 12"><path d="M3 1l2 2.5-1.2 1.3a7 7 0 003.4 3.4L8.5 7 11 9l-1.4 1.8C5 10.5 1.5 7 1.2 2.4z" fill="#fff"/></svg><span class="big">123-456-7890</span></div>
      <div class="foot-row"><svg viewBox="0 0 10 10"><rect x="1" y="2" width="8" height="6" fill="#fff"/></svg><span>hello@brightvalecrew.example</span></div>
    </div>
    <ul class="foot-links"><li>Home</li><li>About us</li><li>Services</li><li>Blog</li><li>Contact</li></ul>
    <div class="foot-social"><i></i><i></i><i></i><i></i></div>
    <p class="foot-copy">© 2021 brightvalecrew</p>
  </footer>
</section>

<!-- ABOUT -->
<section class="mock mock--about" aria-label="About us page">
  <svg class="hero-svg" width="451" height="200" viewBox="0 0 451 200" aria-hidden="true">
    <defs>
      <linearGradient id="aboutBlue" x1="0" y1="0" x2="1" y2="1">
        <stop offset="0" stop-color="#0f2d95"/>
        <stop offset="1" stop-color="#1b45bd"/>
      </linearGradient>
    </defs>
    <path d="M0 0H451V178Q240 140 0 160Z" fill="url(#aboutBlue)"/>
  </svg>
  <nav class="site-nav">
    <div class="brand"><span class="brand-dot"></span>BRIGHTVALE CREW</div>
    <ul class="nav-links"><li>HOME</li><li>ABOUT</li><li>SERVICES</li><li>BLOG</li><li class="is-cta">CONTACT</li></ul>
    <div class="nav-phone"><svg viewBox="0 0 12 12"><path d="M3 1l2 2.5-1.2 1.3a7 7 0 003.4 3.4L8.5 7 11 9l-1.4 1.8C5 10.5 1.5 7 1.2 2.4z" fill="currentColor"/></svg>123-456-7890</div>
  </nav>
  <div class="abs" style="left:63px;top:82px;color:var(--white);font-size:15px;font-weight:500;letter-spacing:.03em">ABOUT US</div>
  <div class="img-block img-device" role="img" aria-label="Laptop showing an analytics dashboard" style="left:250px;top:61px;width:169px;height:109px"></div>

  <div class="section-title" style="left:226px;top:208px;font-size:5px;color:#2a6fe0;font-weight:500">Lorem ipsum</div>
  <div class="section-title" style="left:226px;top:221px;font-size:10px">WHY BRIGHTVALE CREW</div>
  <p class="abs tiny" style="left:79px;top:268px;width:138px;font-size:4.4px">Lorem ipsum dolor sit amet, consectetuer adipiscing elit, sed diam nonummy nibh euismod tincidunt ut laoreet dolore magna aliquam erat volutpat. Ut wisi enim ad minim veniam, quis nostrud exerci tation ullamcorper suscipit lobortis nisl ut aliquip ex ea commodo consequat.<br><br>Duis autem vel eum iriure dolor in hendrerit in vulputate velit esse molestie consequat, vel illum</p>
  <div class="img-block img-photo" role="img" aria-label="Man in a denim shirt working on a laptop" style="left:239px;top:258px;width:169px;height:112px;border-radius:0"></div>

  <div class="section-title" style="left:226px;top:428px;font-size:10px">OUR TEAM</div>
  <div class="img-block img-photo" role="img" aria-label="Portrait of a team member in a suit" style="left:60px;top:464px;width:154px;height:114px;border-radius:0"></div>
  <div class="social-dots" style="left:110px;top:574px"><i></i><i></i><i></i><i></i></div>
  <div class="team-name" style="left:243px;top:477px">Daniel Hart</div>
  <p class="abs tiny" style="left:243px;top:494px;width:122px;font-size:4.2px">Lorem ipsum dolor sit amet, consectetuer adipiscing elit, sed diam nonummy nibh euismod tincidunt ut laoreet dolore magna aliquam erat volutpat. Ut wisi enim ad minim veniam, quis nostrud exerci tation ullamcorper suscipit lobortis nisl ut aliquip ex ea commodo consequat.</p>
  <div class="team-name" style="left:70px;top:630px">Daniel Hart</div>
  <p class="abs tiny" style="left:70px;top:646px;width:122px;font-size:4.2px">Lorem ipsum dolor sit amet, consectetuer adipiscing elit, sed diam nonummy nibh euismod tincidunt ut laoreet dolore magna aliquam erat volutpat. Ut wisi enim ad minim veniam, quis nostrud exerci tation ullamcorper suscipit lobortis nisl ut aliquip ex ea commodo consequat.</p>
  <div class="img-block img-photo" role="img" aria-label="Portrait of a smiling team member in a suit" style="left:227px;top:614px;width:157px;height:112px;border-radius:0"></div>
  <div class="social-dots" style="left:281px;top:722px"><i></i><i></i><i></i><i></i></div>

  <div class="abs" style="left:0;top:760px;width:451px;height:220px;background:var(--mist)"></div>
  <div class="section-title" style="left:320px;top:788px;font-size:10px">OUR VALUES</div>
  <p class="abs tiny" style="left:250px;top:808px;width:140px;text-align:center;font-size:4.2px">Lorem ipsum dolor sit amet, consectetuer adipiscing elit, sed diam nonummy nibh euismod tincidunt ut laoreet dolore magna aliquam erat volutpat.</p>
  <div class="img-block img-photo" role="img" aria-label="Man working at a desktop computer in an office" style="left:38px;top:829px;width:173px;height:127px;border-radius:0"></div>
  <div class="value-item" style="top:856px">Brokers are Better</div>
  <div class="value-item" style="top:889px">Experimentation</div>
  <div class="value-item" style="top:923px">Compliance</div>

  <div class="cta-card" style="left:118px;top:1015px;width:214px;height:102px">
    <h3>Feel Free To Contact Us</h3>
    <p>Lorem ipsum dolor sit amet, consectetuer adipiscing elit. Sed diam dolor eu feugiat nulla facilisis at.</p>
    <div class="btn btn--blue">GET A CALL BACK</div>
  </div>

  <footer class="site-footer" style="height:124px">
    <div class="foot-brand"><span class="brand-dot"></span>BRIGHTVALE CREW</div>
    <div class="foot-contact">
      <div class="foot-row"><svg viewBox="0 0 10 10"><path d="M5 9.5S1.5 5.8 1.5 3.8a3.5 3.5 0 017 0C8.5 5.8 5 9.5 5 9.5z" fill="#fff"/></svg><div><b>BRIGHTVALE CREW</b>Lorem ipsum sit dolor sit<br>amet adipiscing, 1200</div></div>
      <div class="foot-row"><svg viewBox="0 0 12 12"><path d="M3 1l2 2.5-1.2 1.3a7 7 0 003.4 3.4L8.5 7 11 9l-1.4 1.8C5 10.5 1.5 7 1.2 2.4z" fill="#fff"/></svg><span class="big">123-456-7890</span></div>
      <div class="foot-row"><svg viewBox="0 0 10 10"><rect x="1" y="2" width="8" height="6" fill="#fff"/></svg><span>hello@brightvalecrew.example</span></div>
    </div>
    <ul class="foot-links"><li>Home</li><li>About us</li><li>Services</li><li>Blog</li><li>Contact</li></ul>
    <div class="foot-social"><i></i><i></i><i></i><i></i></div>
    <p class="foot-copy">© 2021 brightvalecrew</p>
  </footer>
</section>

<!-- CONTACT -->
<section class="mock mock--contact" aria-label="Contact us page">
  <nav class="site-nav site-nav--light">
    <div class="brand"><span class="brand-dot"></span>BRIGHTVALE CREW</div>
    <ul class="nav-links"><li>HOME</li><li>ABOUT</li><li>SERVICES</li><li>BLOG</li><li class="is-cta">CONTACT</li></ul>
    <div class="nav-phone"><svg viewBox="0 0 12 12"><path d="M3 1l2 2.5-1.2 1.3a7 7 0 003.4 3.4L8.5 7 11 9l-1.4 1.8C5 10.5 1.5 7 1.2 2.4z" fill="currentColor"/></svg>123-456-7890</div>
  </nav>
  <div class="section-title" style="left:227px;top:62px;font-size:10px;font-weight:500">Contact Us</div>
  <svg class="abs" style="left:375px;top:58px" width="79" height="60" viewBox="0 0 79 60" aria-hidden="true">
    <path d="M40 0Q30 45 79 56V60Q20 58 40 0Z" fill="#0f2d95"/>
  </svg>
  <svg class="abs" style="left:35px;top:224px" width="50" height="50" viewBox="0 0 50 50" aria-hidden="true"><circle cx="25" cy="25" r="25" fill="#f4d03c"/></svg>
  <div class="contact-card">
    <div class="contact-panel">
      <h4>Let's Start a<br>Conversation</h4>
      <p>Lorem ipsum dolor sit amet, consectetuer adipiscing elit, sed diam nonummy nibh euismod tincidunt ut laoreet dolore magna aliquam erat volutpat</p>
    </div>
    <div class="abs" style="left:142px;top:17px;font-size:5.2px;font-weight:700">Want to get in touch?</div>
    <p class="abs" style="left:142px;top:27px;width:160px;font-size:4.2px;line-height:1.7;color:var(--grey)">Lorem ipsum dolor sit amet, consectetuer adipiscing elit sed diam nonummy nibh euismod tincidunt ut laoreet dolore<br><span style="color:#2a6fe0">hello@brightvalecrew.example</span></p>
    <div class="contact-input" style="left:142px;top:65px;width:87px;height:14px">Name</div>
    <div class="contact-input" style="left:235px;top:65px;width:87px;height:14px">Email</div>
    <div class="contact-input" style="left:142px;top:87px;width:180px;height:29px">Message</div>
    <div class="btn btn--blue" style="left:142px;top:131px;width:35px;height:13px;font-size:3.8px">SEND</div>
  </div>
  <footer class="site-footer" style="height:92px">
    <div class="foot-brand"><span class="brand-dot"></span>BRIGHTVALE CREW</div>
    <div class="foot-contact">
      <div class="foot-row"><svg viewBox="0 0 10 10"><path d="M5 9.5S1.5 5.8 1.5 3.8a3.5 3.5 0 017 0C8.5 5.8 5 9.5 5 9.5z" fill="#fff"/></svg><div><b>BRIGHTVALE CREW</b>Lorem ipsum sit dolor sit<br>amet adipiscing, 1200</div></div>
      <div class="foot-row"><svg viewBox="0 0 12 12"><path d="M3 1l2 2.5-1.2 1.3a7 7 0 003.4 3.4L8.5 7 11 9l-1.4 1.8C5 10.5 1.5 7 1.2 2.4z" fill="#fff"/></svg><span class="big">123-456-7890</span></div>
      <div class="foot-row"><svg viewBox="0 0 10 10"><rect x="1" y="2" width="8" height="6" fill="#fff"/></svg><span>hello@brightvalecrew.example</span></div>
    </div>
    <ul class="foot-links"><li>Home</li><li>About us</li><li>Services</li><li>Blog</li><li>Contact</li></ul>
    <div class="foot-social"><i></i><i></i><i></i><i></i></div>
    <p class="foot-copy">© 2021 brightvalecrew</p>
  </footer>
</section>

<!-- SERVICES -->
<section class="mock mock--services" aria-label="Services page">
  <svg class="hero-svg" width="453" height="200" viewBox="0 0 453 200" aria-hidden="true">
    <defs>
      <linearGradient id="svcBlue" x1="0" y1="0" x2="1" y2="1">
        <stop offset="0" stop-color="#0f2d95"/>
        <stop offset="1" stop-color="#1b45bd"/>
      </linearGradient>
    </defs>
    <path d="M0 0H453V172Q240 140 0 160Z" fill="url(#svcBlue)"/>
  </svg>
  <nav class="site-nav">
    <div class="brand"><span class="brand-dot"></span>BRIGHTVALE CREW</div>
    <ul class="nav-links"><li>HOME</li><li>ABOUT</li><li>SERVICES</li><li>BLOG</li><li class="is-cta">CONTACT</li></ul>
    <div class="nav-phone"><svg viewBox="0 0 12 12"><path d="M3 1l2 2.5-1.2 1.3a7 7 0 003.4 3.4L8.5 7 11 9l-1.4 1.8C5 10.5 1.5 7 1.2 2.4z" fill="currentColor"/></svg>123-456-7890</div>
  </nav>
  <div class="abs" style="left:63px;top:82px;color:var(--white);font-size:15px;font-weight:500;letter-spacing:.03em">SERVICES</div>
  <div class="img-block img-device" role="img" aria-label="Laptop showing an analytics dashboard" style="left:249px;top:58px;width:175px;height:108px"></div>

  <article class="svc-card" style="left:48px;top:255px">
    <svg viewBox="0 0 26 24"><rect x="2" y="6" width="16" height="14" fill="none" stroke="#12329e"/><path d="M8 14l12-11 3 3-12 11-4 1z" fill="none" stroke="#12329e"/></svg>
    <h4>BRAND DESIGN &amp; STRATEGY</h4>
    <div class="lead">Lorem ipsum dolor sit amet,<br>consectetuer adipiscing elit.</div>
    <p>Lorem ipsum dolor sit amet, consectetuer adipiscing elit, sed diam nonummy nibh euismod tincidunt ut laoreet dolore magna aliquam erat volutpat. Ut wisi enim ad minim veniam, quis nostrud exerci tation ullamcorper suscipit lobortis nisl ut aliquip ex ea commodo consequat.</p>
  </article>
  <article class="svc-card" style="left:48px;top:450px">
    <svg viewBox="0 0 26 24"><circle cx="13" cy="12" r="4" fill="none" stroke="#12329e"/><circle cx="5" cy="5" r="3" fill="none" stroke="#12329e"/><circle cx="21" cy="5" r="3" fill="none" stroke="#12329e"/><circle cx="5" cy="19" r="3" fill="none" stroke="#12329e"/><circle cx="21" cy="19" r="3" fill="none" stroke="#12329e"/></svg>
    <h4>SOCIAL MEDIA MANAGEMENT</h4>
    <div class="lead">Lorem ipsum dolor sit amet,<br>consectetuer adipiscing elit.</div>
    <p>Lorem ipsum dolor sit amet, consectetuer adipiscing elit, sed diam nonummy nibh euismod tincidunt ut laoreet dolore magna aliquam erat volutpat. Ut wisi enim ad minim veniam, quis nostrud exerci tation ullamcorper suscipit lobortis nisl ut aliquip ex ea commodo consequat.</p>
  </article>
  <article class="svc-card" style="left:48px;top:648px">
    <svg viewBox="0 0 26 24"><path d="M3 22V14h4v8M10 22V10h4v12M17 22V6h4v16" fill="none" stroke="#12329e"/><path d="M3 9l7-5 5 3 8-6" fill="none" stroke="#12329e"/></svg>
    <h4>SEO</h4>
    <div class="lead">Lorem ipsum dolor sit amet,<br>consectetuer adipiscing elit.</div>
    <p>Lorem ipsum dolor sit amet, consectetuer adipiscing elit, sed diam nonummy nibh euismod tincidunt ut laoreet dolore magna aliquam erat volutpat. Ut wisi enim ad minim veniam, quis nostrud exerci tation ullamcorper suscipit lobortis nisl ut aliquip ex ea commodo consequat.</p>
  </article>
  <article class="svc-card" style="left:48px;top:844px">
    <svg viewBox="0 0 26 24"><circle cx="13" cy="12" r="10" fill="none" stroke="#12329e"/><path d="M3 12h20M13 2c-5 6-5 14 0 20M13 2c5 6 5 14 0 20" fill="none" stroke="#12329e"/></svg>
    <h4>REPUTATION MANAGEMENT</h4>
    <div class="lead">Lorem ipsum dolor sit amet,<br>consectetuer adipiscing elit.</div>
    <p>Lorem ipsum dolor sit amet, consectetuer adipiscing elit, sed diam nonummy nibh euismod tincidunt ut laoreet dolore magna aliquam erat volutpat. Ut wisi enim ad minim veniam, quis nostrud exerci tation ullamcorper suscipit lobortis nisl ut aliquip ex ea commodo consequat.</p>
  </article>

  <article class="svc-card" style="left:237px;top:215px">
    <svg viewBox="0 0 26 24"><rect x="5" y="6" width="18" height="13" fill="none" stroke="#12329e"/><path d="M5 6l9 7 9-7M1 10h3M0 14h4" fill="none" stroke="#12329e"/></svg>
    <h4>EMAIL MARKETING</h4>
    <div class="lead">Lorem ipsum dolor sit amet,<br>consectetuer adipiscing elit.</div>
    <p>Lorem ipsum dolor sit amet, consectetuer adipiscing elit, sed diam nonummy nibh euismod tincidunt ut laoreet dolore magna aliquam erat volutpat. Ut wisi enim ad minim veniam, quis nostrud exerci tation ullamcorper suscipit lobortis nisl ut aliquip ex ea commodo consequat.</p>
  </article>
  <article class="svc-card" style="left:237px;top:412px">
    <svg viewBox="0 0 26 24"><rect x="2" y="2" width="14" height="11" rx="2" fill="none" stroke="#12329e"/><rect x="10" y="9" width="14" height="11" rx="2" fill="none" stroke="#12329e"/><path d="M6 7h6M14 14h6" stroke="#12329e"/></svg>
    <h4>MORTGAGE CHATBOT</h4>
    <div class="lead">Lorem ipsum dolor sit amet,<br>consectetuer adipiscing elit.</div>
    <p>Lorem ipsum dolor sit amet, consectetuer adipiscing elit, sed diam nonummy nibh euismod tincidunt ut laoreet dolore magna aliquam erat volutpat. Ut wisi enim ad minim veniam, quis nostrud exerci tation ullamcorper suscipit lobortis nisl ut aliquip ex ea commodo consequat.</p>
  </article>
  <article class="svc-card" style="left:237px;top:609px">
    <svg viewBox="0 0 26 24"><circle cx="13" cy="12" r="5" fill="none" stroke="#12329e"/><path d="M13 1v5M13 18v5M2 12h6M18 12h6M5 4l4 4M17 16l4 4M21 4l-4 4M9 16l-4 4" stroke="#12329e"/></svg>
    <h4>CONTENT MARKETING</h4>
    <div class="lead">Lorem ipsum dolor sit amet,<br>consectetuer adipiscing elit.</div>
    <p>Lorem ipsum dolor sit amet, consectetuer adipiscing elit, sed diam nonummy nibh euismod tincidunt ut laoreet dolore magna aliquam erat volutpat. Ut wisi enim ad minim veniam, quis nostrud exerci tation ullamcorper suscipit lobortis nisl ut aliquip ex ea commodo consequat.</p>
  </article>
  <article class="svc-card" style="left:237px;top:804px">
    <svg viewBox="0 0 26 24"><rect x="1" y="2" width="14" height="9" fill="none" stroke="#12329e"/><path d="M8 22v-6h4v6M14 22v-9h4v9M20 22V9h4v13" fill="none" stroke="#12329e"/></svg>
    <h4>WEBSITE DEVELOPMENT</h4>
    <div class="lead">Lorem ipsum dolor sit amet,<br>consectetuer adipiscing elit.</div>
    <p>Lorem ipsum dolor sit amet, consectetuer adipiscing elit, sed diam nonummy nibh euismod tincidunt ut laoreet dolore magna aliquam erat volutpat. Ut wisi enim ad minim veniam, quis nostrud exerci tation ullamcorper suscipit lobortis nisl ut aliquip ex ea commodo consequat.</p>
  </article>

  <div class="cta-card" style="left:116px;top:1048px;width:221px;height:102px">
    <h3>Feel Free To Contact Us</h3>
    <p>Lorem ipsum dolor sit amet, consectetuer adipiscing elit. Sed diam dolor eu feugiat nulla facilisis at.</p>
    <div class="btn btn--blue">GET A CALL BACK</div>
  </div>

  <footer class="site-footer" style="height:127px">
    <div class="foot-brand"><span class="brand-dot"></span>BRIGHTVALE CREW</div>
    <div class="foot-contact">
      <div class="foot-row"><svg viewBox="0 0 10 10"><path d="M5 9.5S1.5 5.8 1.5 3.8a3.5 3.5 0 017 0C8.5 5.8 5 9.5 5 9.5z" fill="#fff"/></svg><div><b>BRIGHTVALE CREW</b>Lorem ipsum sit dolor sit<br>amet adipiscing, 1200</div></div>
      <div class="foot-row"><svg viewBox="0 0 12 12"><path d="M3 1l2 2.5-1.2 1.3a7 7 0 003.4 3.4L8.5 7 11 9l-1.4 1.8C5 10.5 1.5 7 1.2 2.4z" fill="#fff"/></svg><span class="big">123-456-7890</span></div>
      <div class="foot-row"><svg viewBox="0 0 10 10"><rect x="1" y="2" width="8" height="6" fill="#fff"/></svg><span>hello@brightvalecrew.example</span></div>
    </div>
    <ul class="foot-links"><li>Home</li><li>About us</li><li>Services</li><li>Blog</li><li>Contact</li></ul>
    <div class="foot-social"><i></i><i></i><i></i><i></i></div>
    <p class="foot-copy">© 2021 brightvalecrew</p>
  </footer>
</section>

</body>
</html>
```